Voltren Assemblies, Inc. Business Card

Voltren has three operating entities and I'm looking for a standard business card template that can be used for Voltren and the three operating entities that the logo just get swapped out, but has a very similar look and feel. Ultimately if someone had a business card from each, they assume the organizations are related because they all have the same look and feel.
Below are our websites and I will attached the logos for each entity:
https://www.voltrenassemblies-example.com/
https://www.brackwayceramic-example.com/
https://www.omdr-pqsx-example.com/
https://www.tamberlinebreaker-example.com/

Target Market(s)

US Voltren

Industry/Entity Type

US Voltren

Contact Information for Business Card

Normal stuff

```html
<!DOCTYPE html>
<html lang="en">
<head>
<meta charset="utf-8">
<title>Voltren Assemblies, Inc. Business Card</title>
<link rel="stylesheet" href="https://fonts.googleapis.com/css2?family=Open+Sans:wght@400;600;700&display=swap">
<style>
  :root{
    --backdrop:#dcdcda;
    --paper:#ffffff;
    --ink-navy:#1f2a6b;
    --ink-grey:#5a5a5a;
    --accent-red:#c8202f;
    --tile-voltren:#243073;
    --tile-brackway-top:#2f63aa;
    --tile-brackway-bottom:#1f4488;
    --tile-omdr:#22205f;
    --tile-tamberline:#4d7490;
    --on-tile:#ffffff;
    --on-tile-soft:#dfe6f2;
  }
  *{box-sizing:border-box;margin:0;padding:0}
  html,body{width:1200px;height:801px;overflow:hidden}
  body{background:var(--backdrop);font-family:"Open Sans",sans-serif;display:flex;align-items:center;justify-content:center;gap:40px}
  .card{width:540px;height:309px;box-shadow:0 6px 18px rgba(0,0,0,.18);position:relative;overflow:hidden}
  .card--front{background:var(--paper);border-bottom:3px solid var(--ink-navy);display:flex;align-items:center}
  .identity{width:260px;text-align:right;padding-right:22px;border-right:1.5px solid var(--ink-navy)}
  .identity__name{font-weight:700;font-size:24px;letter-spacing:.5px;color:var(--ink-navy);text-transform:uppercase}
  .identity__title{font-size:15px;color:var(--ink-grey)}
  .contact{padding-left:20px;font-size:13px;line-height:1.55;color:var(--ink-grey)}
  .contact__address{margin-bottom:4px}
  .contact__row{display:flex;align-items:center;gap:7px}
  .contact__row svg{width:11px;height:11px;fill:var(--accent-red);flex:none}
  .card--back{display:grid;grid-template-columns:1fr 1fr;grid-template-rows:1fr 1fr}
  .tile{display:flex;flex-direction:column;align-items:center;justify-content:center;color:var(--on-tile);text-align:center;padding:10px}
  .tile--voltren{background:var(--tile-voltren)}
  .tile--brackway{background:linear-gradient(180deg,var(--tile-brackway-top),var(--tile-brackway-bottom))}
  .tile--omdr{background:var(--tile-omdr)}
  .tile--tamberline{background:var(--tile-tamberline)}
  .brand{display:flex;align-items:center;gap:8px;font-weight:700;font-size:20px;letter-spacing:.5px;text-transform:uppercase}
  .brand__mark{width:16px;height:16px;background:var(--on-tile);flex:none}
  .brand__mark--round{border-radius:50%}
  .tile__tagline{font-size:9px;color:var(--on-tile-soft);margin-top:3px}
  .tile__url{font-size:12px;margin-top:8px}
</style>
</head>
<body>
  <section class="card card--front" aria-label="Card front">
    <div class="identity">
      <h1 class="identity__name">Darren Keswick</h1>
      <p class="identity__title">President</p>
    </div>
    <div class="contact">
      <p class="contact__address">2480 Halvern Road<br>Suite 210, Fairmont, AL 35190</p>
      <p class="contact__row"><svg viewBox="0 0 12 12" aria-hidden="true"><path d="M2 1l2.5 0 1 3-1.5 1a7 7 0 0 0 3 3l1-1.5 3 1V10A1 1 0 0 1 10 11 9 9 0 0 1 1 2 1 1 0 0 1 2 1z"/></svg>555 014 2276</p>
      <p class="contact__row"><svg viewBox="0 0 12 12" aria-hidden="true"><path d="M1 3h10v6H1z M1 3l5 3.5L11 3"/></svg>info@voltrenassemblies-example.com</p>
      <p class="contact__row"><svg viewBox="0 0 12 12" aria-hidden="true"><circle cx="6" cy="6" r="5"/></svg>www.voltrenassemblies-example.com</p>
    </div>
  </section>

  <section class="card card--back" aria-label="Card back">
    <div class="tile tile--voltren">
      <p class="brand"><span class="brand__mark brand__mark--round"></span>Voltren</p>
      <p class="tile__tagline">Assemblies, Inc.</p>
      <p class="tile__url">www.voltrenassemblies-example.com</p>
    </div>
    <div class="tile tile--brackway">
      <p class="brand"><span class="brand__mark"></span>Brackway Ceramic, LLC</p>
      <p class="tile__tagline">A Voltren Assemblies, Inc. Company</p>
      <p class="tile__url">www.brackwayceramic-example.com</p>
    </div>
    <div class="tile tile--omdr">
      <p class="brand"><span class="brand__mark"></span>OMDR</p>
      <p class="tile__tagline">Orwen Metering Device Resources<br>A Voltren Assemblies, Inc. Company</p>
      <p class="tile__url">www.omdr-pqsx-example.com</p>
    </div>
    <div class="tile tile--tamberline">
      <p class="brand"><span class="brand__mark"></span>Tamberline Breaker</p>
      <p class="tile__tagline">A Voltren Assemblies, Inc. Company</p>
      <p class="tile__url">www.tamberlinebreaker-example.com</p>
    </div>
  </section>
</body>
</html>
```